female esthetician looking for an impact business card

I an an expert in skin care industry with high experience in NYC.I want my business card to look professional , an impact at first look. I do want a combination between white and gold . I believe the font will be great if is gold.. The Fonts are also important. MARISELA VONDRAKE (SKIN CARE BOUTIQUE)

THIS SHOULD BE THE BUSINESS NAME, and should be placed on th eback of the card.
IN front m, the name MARISELA VONDRAKE - ESTHETCIAN

BY APPOINTMENTS ONLY: 555.218.9031

Target Market(s)

HIGH END CLIENTELE

Contact Information for Business Card

iT WILL BE on a luxury paper. I neeed the wow feeling

Requirements
Should not have
• pictures

```html
<!DOCTYPE html>
<html lang="en">
<head>
<meta charset="utf-8">
<title>Marisela Vondrake — Business Card</title>
<link rel="stylesheet" href="https://fonts.googleapis.com/css2?family=Josefin+Sans:wght@300;400&family=Questrial&display=swap">
<style>
  :root {
    --backdrop: #ebe7e0;
    --paper: #fdfbf3;
    --paper-edge: #e6e1d3;
    --damask-tone: #f3efe2;
    --monogram-tone: #efebe0;
    --gold: #b38a36;
    --gold-line: #c9a65a;
    --ink: #2a2622;
  }
  * { box-sizing: border-box; margin: 0; padding: 0; }
  html, body {
    width: 1200px;
    height: 800px;
    overflow: hidden;
    background: var(--backdrop);
  }
  .canvas {
    position: relative;
    width: 1200px;
    height: 800px;
    display: flex;
    align-items: center;
    justify-content: center;
    gap: 60px;
  }
  .card {
    position: relative;
    width: 525px;
    height: 300px;
    background: var(--paper);
    border: 1px solid var(--paper-edge);
    box-shadow: 0 10px 24px rgba(60, 45, 25, 0.14);
    overflow: hidden;
  }

  /* Front: esthetician details */
  .card--front .monogram-field {
    position: absolute;
    left: 155px;
    top: 40px;
    width: 200px;
    height: 200px;
    border-radius: 50%;
    background: var(--monogram-tone);
  }
  .card--front .details {
    position: absolute;
    left: 0;
    right: 0;
    top: 100px;
    text-align: center;
  }
  .card--front .name {
    font-family: "Josefin Sans", sans-serif;
    font-weight: 300;
    font-size: 24px;
    letter-spacing: 0.04em;
    color: var(--gold);
    line-height: 1;
  }
  .card--front .role {
    font-family: "Questrial", sans-serif;
    font-size: 9px;
    letter-spacing: 0.08em;
    color: var(--ink);
    margin-top: 3px;
    padding-left: 120px;
  }
  .card--front .appointments {
    font-family: "Questrial", sans-serif;
    font-size: 12px;
    letter-spacing: 0.03em;
    color: var(--ink);
    margin-top: 22px;
  }
  .card--front .phone {
    font-family: "Questrial", sans-serif;
    font-size: 21px;
    letter-spacing: 0.04em;
    color: var(--ink);
    margin-top: 3px;
  }

  /* Back: boutique name */
  .card--back .damask-field {
    position: absolute;
    inset: 0;
    background: radial-gradient(ellipse at center, var(--paper) 0%, var(--damask-tone) 100%);
  }
  .card--back .name-band {
    position: absolute;
    left: 0;
    right: 0;
    top: 108px;
    height: 84px;
    background: var(--paper);
    border-top: 1.5px solid var(--gold-line);
    border-bottom: 1.5px solid var(--gold-line);
  }
  .card--back .boutique-name {
    position: absolute;
    left: 0;
    right: 0;
    top: 124px;
    text-align: center;
    font-family: "Josefin Sans", sans-serif;
    font-weight: 300;
    color: var(--gold);
  }
  .card--back .boutique-name .primary {
    display: block;
    font-size: 30px;
    letter-spacing: 0.04em;
    line-height: 1;
  }
  .card--back .boutique-name .secondary {
    display: block;
    font-size: 12px;
    letter-spacing: 0.22em;
    margin-top: 6px;
  }
</style>
</head>
<body>
<main class="canvas">
  <section class="card card--front" aria-label="Card front">
    <div class="monogram-field" aria-hidden="true"></div>
    <div class="details">
      <p class="name">MARISELA VONDRAKE</p>
      <p class="role">ESTHETICIAN</p>
      <p class="appointments">BY APPOINTMENTS ONLY</p>
      <p class="phone">555.218.9031</p>
    </div>
  </section>

  <section class="card card--back" aria-label="Card back">
    <div class="damask-field" role="img" aria-label="Soft ivory damask floral pattern covering the card"></div>
    <div class="name-band"></div>
    <p class="boutique-name">
      <span class="primary">MARISELA VONDRAKE</span>
      <span class="secondary">SKIN CARE BOUTIQUE</span>
    </p>
  </section>
</main>
</body>
</html>
```